Harlow Crest Holdings (Remodeling company) needs a logo and business card

We need a business card design for a new company. We "flip" upmarket houses (buy, remodel and sell) in the Austin, TX area. I'd like neutral colors (grey, white, gold black). I would like it to include a simple, clean logo. Our designs are modern and uncluttered and I would like that reflected in the business card design.

Target Market(s)

Young professionals, Families, Retirees. Our properties will sell for $750k+

Industry/Entity Type

Real Estate

Contact Information for Business Card

Harlow Crets Holdings
Mona Harlow
(979) 555 0142
Owner
Rolf Tandem
(512) 555 0176
Realtor

Logo Text

Harlow Crest Holdings

Font styles to use
Serif
Script

Requirements
Must have
• Simple, classic design
Nice to have
• Clean lines, modern look
Should not have
• Too traditionally

```html
<!DOCTYPE html>
<html lang="en">
<head>
<meta charset="utf-8">
<title>Harlow Crest Holdings – Business Card</title>
<link href="https://fonts.googleapis.com/css2?family=Cinzel:wght@600&family=Source+Sans+3:wght@400;600&display=swap" rel="stylesheet">
<style>
  :root {
    --backdrop: #e4e4e4;
    --card: #050505;
    --gold: #e5b010;
    --white: #ffffff;
  }
  * { box-sizing: border-box; margin: 0; padding: 0; }
  html, body { width: 1200px; height: 900px; overflow: hidden; }
  body {
    background: var(--backdrop);
    position: relative;
    font-family: "Source Sans 3", Arial, sans-serif;
  }
  .card {
    position: absolute;
    top: 306px;
    width: 440px;
    height: 271px;
    background: var(--card);
    border-radius: 12px;
  }
  .card--front { left: 149px; }
  .card--back { left: 608px; }

  .brand-name {
    position: absolute;
    left: 0; right: 0;
    text-align: center;
    font-family: "Cinzel", Georgia, serif;
    font-weight: 600;
    color: var(--gold);
    letter-spacing: 0.06em;
    line-height: 1.15;
  }
  .card--front .brand-name { top: 48px; font-size: 25px; }
  .card--back .brand-name { top: 102px; font-size: 32px; }

  .contact {
    position: absolute;
    left: 23px;
    right: 24px;
    display: flex;
    justify-content: space-between;
    align-items: flex-end;
  }
  .contact--realtor { top: 151px; }
  .contact--owner { top: 205px; }
  .contact__name {
    display: block;
    color: var(--gold);
    font-weight: 600;
    font-size: 16px;
    line-height: 20px;
  }
  .contact__role {
    display: block;
    color: var(--white);
    font-size: 12px;
    line-height: 16px;
  }
  .contact__phone {
    display: flex;
    align-items: center;
    gap: 5px;
    color: var(--white);
    font-size: 12px;
    margin-bottom: 14px;
  }
  .contact__phone svg { width: 10px; height: 10px; fill: var(--gold); }
</style>
</head>
<body>
  <section class="card card--front">
    <div class="brand-name">HARLOW CRETS<br>HOLDINGS</div>

    <div class="contact contact--realtor">
      <div>
        <span class="contact__name">Rolf Tandem</span>
        <span class="contact__role">Realtor</span>
      </div>
      <div class="contact__phone">(512) 555 0176
        <svg viewBox="0 0 10 10" aria-hidden="true"><path d="M1 3.5C1 2 3 1.5 5 1.5S9 2 9 3.5v1H7V3.3H3v1.2H1z M2.5 5h5l1 3.5h-7z"/></svg>
      </div>
    </div>

    <div class="contact contact--owner">
      <div>
        <span class="contact__name">Mona Harlow</span>
        <span class="contact__role">Owner</span>
      </div>
      <div class="contact__phone">(979) 555 0142
        <svg viewBox="0 0 10 10" aria-hidden="true"><path d="M1 3.5C1 2 3 1.5 5 1.5S9 2 9 3.5v1H7V3.3H3v1.2H1z M2.5 5h5l1 3.5h-7z"/></svg>
      </div>
    </div>
  </section>

  <section class="card card--back">
    <div class="brand-name">HARLOW CRETS<br>HOLDINGS</div>
  </section>
</body>
</html>
```